certificate to present to patients after successful vasectomy

creation of a A4 sized colour certificate that can be presented to patients after their three month semen test confirms a successful vasectomy.
I have attached my current logo for Clearway Snip Clinic with the colours blue and green. I have attached a collage of example fun images related to congratulating men after their vasectomy.

Target Market(s)

A fun certificate to provide to men after a successful vasectomy. THis is a bit more playful/fun than traditional medical illustration/medical information. Men can stick it on the fridge or wave it about a family events to mortify their children.

Font styles to use
Sans Serif

Colors

Designer to choose colors to be used in the design.

Requirements
Must have
• Clearway Snip Clinic Logo and these or complimentary colours
• Be editable to add the patients name and date of certificate
Nice to have
• continuation of design themes from logo
Should not have
• should not have realistic or medical illustration of penis/scrotum. This should be a fun/silly certificate they can put on the family fridge or cork board

```html
<!DOCTYPE html>
<html lang="en">
<head>
<meta charset="utf-8">
<title>Vasectomy Success Certificate</title>
<link rel="stylesheet" href="https://fonts.googleapis.com/css2?family=Quicksand:wght@500;600;700&family=Parisienne&display=swap">
<style>
  :root {
    --frame-cyan: #3fd6f5;
    --paper: #eef8fc;
    --brand-blue: #1b5f93;
    --brand-light-blue: #2a86c8;
    --lime: #7ed321;
    --ink: #161616;
    --muted-ink: #4a4a4a;
    --white: #ffffff;
    --art-dark: #3a3a3c;
    --art-blue: #8fcdea;
    --art-red: #e9a0a3;
  }
  * { margin: 0; padding: 0; box-sizing: border-box; }
  html, body { width: 849px; height: 1200px; overflow: hidden; background: var(--white); }
  .certificate {
    position: relative;
    width: 849px;
    height: 1200px;
    background: var(--paper);
    border: 4px solid var(--frame-cyan);
    box-shadow: inset 0 0 22px 10px rgba(63, 214, 245, 0.55);
    font-family: "Quicksand", sans-serif;
    overflow: hidden;
  }
  .hero-illustration {
    position: absolute;
    left: 167px;
    top: 115px;
    width: 366px;
    height: 466px;
    border-radius: 24px;
    background: linear-gradient(180deg, rgba(58,58,60,0.22) 0%, rgba(143,205,234,0.35) 62%, rgba(233,160,163,0.35) 100%);
  }
  .headline {
    position: absolute;
    right: 82px;
    top: 606px;
    font-size: 44px;
    font-weight: 600;
    letter-spacing: 2px;
    line-height: 1.2;
    color: var(--brand-blue);
  }
  .patient-name {
    position: absolute;
    left: 0;
    right: 78px;
    top: 672px;
    text-align: right;
    font-family: "Parisienne", cursive;
    font-size: 134px;
    line-height: 1.2;
    color: var(--lime);
  }
  .achievement {
    position: absolute;
    right: 84px;
    top: 852px;
    font-size: 30px;
    font-weight: 500;
    letter-spacing: 3px;
    line-height: 1.2;
    color: var(--ink);
  }
  .certificate-date {
    position: absolute;
    right: 84px;
    top: 910px;
    font-size: 18px;
    font-weight: 500;
    letter-spacing: 1.5px;
    color: var(--muted-ink);
  }
  .clinic-mark {
    position: absolute;
    left: 42px;
    top: 1046px;
    display: flex;
    align-items: center;
    gap: 14px;
  }
  .clinic-mark-square {
    width: 24px;
    height: 24px;
    background: var(--brand-light-blue);
  }
  .clinic-mark-name {
    font-size: 32px;
    font-weight: 700;
    line-height: 1.1;
    color: var(--brand-light-blue);
  }
  .signature {
    position: absolute;
    left: 553px;
    top: 979px;
    width: 176px;
    height: 90px;
    border-radius: 10px;
    background: linear-gradient(90deg, rgba(22,22,22,0.06), rgba(22,22,22,0.13), rgba(22,22,22,0.06));
  }
  .signatory {
    position: absolute;
    left: 502px;
    width: 284px;
    top: 1094px;
    text-align center;
    text-align: center;
  }
  .signatory-name {
    font-size: 21px;
    font-weight: 500;
    color: var(--ink);
  }
  .signatory-clinic {
    margin-top: 4px;
    font-size: 17px;
    font-weight: 700;
    color: var(--brand-light-blue);
  }
</style>
</head>
<body>
  <main class="certificate">
    <div class="hero-illustration" role="img" aria-label="Illustration of a black water tap with a thin blue stream stopped by a red CLOSED stamp"></div>

    <h1 class="headline">CONGRATULATIONS!</h1>
    <p class="patient-name">John Doe</p>
    <p class="achievement">had a successful vasectomy!</p>
    <p class="certificate-date">Date: 14 June 2025</p>

    <div class="clinic-mark">
      <span class="clinic-mark-square"></span>
      <span class="clinic-mark-name">Clearway<br>Snip Clinic</span>
    </div>

    <div class="signature" role="img" aria-label="Handwritten doctor's signature"></div>
    <div class="signatory">
      <p class="signatory-name">Dr Martin Hale</p>
      <p class="signatory-clinic">CLEARWAY SNIP CLINIC</p>
    </div>
  </main>
</body>
</html>
```